Spiritual Self Help Book Cover

I need a book cover that's extremely appealing to spiritual seekers, self-help/health and wellness fans. Mostly for women.
The book blends spirituality/mysticism with science for readers to understand how to optimize their health/body, emotional well-being, mental wellness, spiritual fulfillment, relationships, business and purpose in life. It infuses ancient and modern understanding of energy/frequency/quantum mechanics along with the science of chiropractic and psychology.
Book title: Folding Every Lantern Inward
I'll attach some examples that are similar to what I like but I want something different and more extravagantly beautiful.
Please use the graphic of the Sri Yantra Mandala into the cover instead of this stock image one.
I'll need the book cover in all formats: paperback, hardcover, ebook and audiobook.
I'll provide the rest of the details, including publisher logo, synopsis, author photo/blurb and ISBN after I pick the final wniner.
Mostly women spiritual seekers, self-help readers, health/wellness enthusiasts

```html
<!DOCTYPE html>
<html lang="en">
<head>
<meta charset="utf-8">
<title>Folding Every Lantern Inward — Book Cover</title>
<link rel="stylesheet" href="https://fonts.googleapis.com/css2?family=Montserrat:wght@400;700;800&family=Oswald:wght@500&display=swap">
<style>
  :root {
    --ink: #1c3a4a;
    --lavender: #c9b2f7;
    --violet: #b99af2;
    --pink: #f6c2f2;
    --blush: #fbe3fb;
    --white: #fdf8ff;
    --aqua: #c4f1fb;
    --magenta: #e56fd2;
    --gold: #f7e27a;
  }
  * { margin: 0; padding: 0; box-sizing: border-box; }
  html, body { width: 849px; height: 1200px; overflow: hidden; }
  body { background: var(--white); }

  .cover {
    position: relative;
    width: 849px;
    height: 1200px;
    overflow: hidden;
    background:
      radial-gradient(ellipse 420px 360px at 15% 8%, rgba(185,154,242,0.85), transparent 70%),
      radial-gradient(ellipse 380px 420px at 60% 6%, rgba(201,178,247,0.8), transparent 70%),
      radial-gradient(ellipse 300px 380px at 100% 55%, rgba(170,235,252,0.9), transparent 70%),
      radial-gradient(ellipse 420px 480px at 5% 45%, rgba(246,160,236,0.75), transparent 70%),
      radial-gradient(ellipse 500px 420px at 30% 95%, rgba(248,200,246,0.7), transparent 70%),
      radial-gradient(ellipse 420px 300px at 55% 48%, rgba(255,255,255,0.95), transparent 70%),
      linear-gradient(180deg, var(--lavender) 0%, var(--pink) 45%, var(--blush) 100%);
  }

  .title {
    position: absolute;
    left: 0;
    width: 100%;
    text-align: center;
    color: var(--ink);
    line-height: 1;
  }
  .title__lead {
    top: 148px;
    font-family: "Montserrat", sans-serif;
    font-weight: 800;
    font-size: 58px;
    letter-spacing: 0.01em;
  }
  .title__middle {
    top: 222px;
    font-family: "Oswald", sans-serif;
    font-weight: 500;
    font-size: 132px;
    letter-spacing: 0.33em;
    padding-left: 0.33em;
  }
  .title__main {
    top: 372px;
    font-family: "Montserrat", sans-serif;
    font-weight: 800;
    font-size: 166px;
    letter-spacing: -0.01em;
  }

  .mandala-art {
    position: absolute;
    left: 89px;
    top: 583px;
    width: 656px;
    height: 582px;
    border-radius: 50%;
    background: radial-gradient(circle at 50% 50%,
      rgba(80,190,90,0.55) 0%,
      rgba(247,226,122,0.75) 14%,
      rgba(245,150,110,0.6) 30%,
      rgba(229,111,210,0.5) 50%,
      rgba(150,110,220,0.35) 72%,
      rgba(90,170,230,0.2) 88%,
      transparent 100%);
  }

  .author {
    position: absolute;
    left: 0;
    width: 100%;
    top: 1012px;
    text-align: center;
    font-family: "Montserrat", sans-serif;
    font-weight: 400;
    font-size: 28px;
    letter-spacing: 0.42em;
    padding-left: 0.42em;
    color: var(--ink);
  }
</style>
</head>
<body>
  <main class="cover">
    <h1>
      <span class="title title__lead">FOLDING EVERY</span>
      <span class="title title__middle">LANTERN</span>
      <span class="title title__main">INWARD</span>
    </h1>
    <div class="mandala-art" role="img" aria-label="Rainbow line-art mandala in blue, violet, pink, orange, yellow and green"></div>
    <p class="author">DR. MARISOL WHITCOMBE</p>
  </main>
</body>
</html>
```